immediate money for financial solutions

We need a Clean yet, eye catching, Business Card denoting a professional financial/tech firm. The front should have our logo and the notion that we are money lenders that get business loans quickly & easily. Maybe shade the colors of our logo. We are opened, but not committed to an unusual shaped card. The Back Should have our Business Contact Info & logo found on our website's front page: TALVOROINC.COM

Financial

```html
<!DOCTYPE html>
<html lang="en">
<head>
<meta charset="utf-8">
<title>Talvoro Inc – Business Card</title>
<link href="https://fonts.googleapis.com/css2?family=Lato:wght@400;700&display=swap" rel="stylesheet">
<style>
  :root {
    --backdrop: #1f1f21;
    --card: #ffffff;
    --green: #2fa84a;
    --green-dark: #238a3a;
    --teal: #2a9d78;
    --ink: #1b1b1b;
  }
  * { margin: 0; padding: 0; box-sizing: border-box; }
  html, body {
    width: 1200px; height: 800px; overflow: hidden;
    background: var(--backdrop);
    font-family: "Lato", sans-serif;
  }
  .canvas {
    position: relative; width: 1200px; height: 800px;
    display: flex; align-items: center; justify-content: center; gap: 60px;
  }
  .card {
    position: relative; width: 500px; height: 286px;
    background: var(--card); overflow: hidden;
  }
  /* Contact side */
  .contact-card .band { position: absolute; inset: 0; }
  .holder {
    position: absolute; top: 34px; right: 40px; text-align: right; color: var(--ink);
  }
  .holder-name { font-size: 19px; font-weight: 400; letter-spacing: .3px; }
  .holder-title { font-size: 10.5px; margin-top: 2px; }
  .wordmark {
    display: flex; align-items: center; gap: 8px;
    color: var(--teal); font-weight: 700; letter-spacing: 1px;
  }
  .wordmark-dot { background: var(--teal); }
  .contact-card .wordmark { position: absolute; left: 36px; top: 100px; font-size: 20px; }
  .contact-card .wordmark-dot { width: 14px; height: 14px; }
  .contact-list {
    position: absolute; left: 36px; top: 150px; list-style: none;
    font-size: 12.5px; color: var(--ink); line-height: 17px;
  }
  .contact-list li { display: flex; align-items: center; gap: 8px; }
  .contact-icon { width: 11px; height: 11px; flex: none; }
  /* Logo side */
  .logo-card { display: flex; align-items: center; justify-content: center; }
  .logo-card .wordmark { font-size: 34px; gap: 14px; }
  .logo-card .wordmark-dot { width: 22px; height: 22px; }
</style>
</head>
<body>
<main class="canvas">
  <section class="card contact-card" aria-label="Contact side">
    <svg class="band" width="500" height="286" viewBox="0 0 500 286" aria-hidden="true">
      <circle cx="500" cy="0" r="14" fill="var(--green)"/>
      <path d="M0 232 L218 232 C244 232 246 196 272 196 L500 196" fill="none" stroke="var(--green)" stroke-width="1.5"/>
      <path d="M0 240 L220 240 C248 240 250 204 278 204 L500 204 L500 244 L0 270 Z" fill="var(--green)"/>
      <path d="M0 276 L500 250" stroke="var(--green-dark)" stroke-width="1.2"/>
    </svg>
    <div class="holder">
      <p class="holder-name">Daniel Marsh</p>
      <p class="holder-title">President/Lender</p>
    </div>
    <div class="wordmark"><span class="wordmark-dot"></span>TALVORO INC</div>
    <ul class="contact-list">
      <li>
        <svg class="contact-icon" viewBox="0 0 12 12"><rect width="12" height="12" rx="2" fill="var(--green)"/><path d="M3 3.5c0 3 2.5 5.5 5.5 5.5l.5-1.5-1.6-.8-.8.8c-1-.4-1.7-1.1-2.1-2.1l.8-.8L4.5 3Z" fill="#fff"/></svg>
        555.014.2290
      </li>
      <li>
        <svg class="contact-icon" viewBox="0 0 12 12"><rect width="12" height="12" rx="2" fill="var(--green)"/><path d="M2.5 3.5h7v5h-7Z M2.5 3.5 6 6.5 9.5 3.5" fill="none" stroke="#fff" stroke-width=".9"/></svg>
        daniel@talvoroinc.com
      </li>
      <li>
        <svg class="contact-icon" viewBox="0 0 12 12"><rect width="12" height="12" rx="2" fill="var(--green)"/><path d="M2.5 3.5h7v5h-7Z M2.5 3.5 6 6.5 9.5 3.5" fill="none" stroke="#fff" stroke-width=".9"/></svg>
        info@talvoroinc.com
      </li>
      <li>
        <svg class="contact-icon" viewBox="0 0 12 12"><circle cx="6" cy="6" r="6" fill="var(--green)"/><path d="M1.5 6h9M6 1.5c-2 2.5-2 6.5 0 9M6 1.5c2 2.5 2 6.5 0 9" fill="none" stroke="#fff" stroke-width=".8"/></svg>
        www.TALVOROINC.COM
      </li>
    </ul>
  </section>

  <section class="card logo-card" aria-label="Logo side">
    <div class="wordmark"><span class="wordmark-dot"></span>TALVORO INC</div>
  </section>
</main>
</body>
</html>
```